Brindlemar Needs Several Greeting Card Shell Designs and Designs for 8.5" x 11" Prints

Brindlemar Ltd. Co. is a publisher of social expression in the form of acrostic poems on greeting cards, prints, mugs, T-shirts, and a host of other products. "Acrostic" simply means spelling out something going down the page. ALL of our products are done in the acrostic style.
We have the following needs:
1) Three feminine greeting card shells designs. One design should allow for up to six lines of text to be added later. The other two designs should allow for up to 10 lines of text to be added later. These designs will be mostly aimed at tweens to young adults.
2)Three masculine greeting card shells designs. One design should allow for up to six lines of text to be added later. The other two designs should allow for up to 10 lines of text to be added later. These designs will be mostly aimed at tweens to young adults.
3) Three feminine design shells for 8.5" x 11" prints, with room for text to be added later. These designs will be aimed at a more mature audience (young adults and up).
4) Three neutral design shells for 8.5" x 11" prints, with room for text to be added later. Three feminine design shells for 8.5" x 11" prints, with room for text to be added later. These designs will be aimed at a more mature audience (young adults and up).
For samples of previous designs, please go to http://www.brindlemar.biz. We are looking for more current, trendy designs.

```html
<!DOCTYPE html>
<html lang="en">
<head>
<meta charset="utf-8">
<title>Brindlemar Greeting Card Shells</title>
<link href="https://fonts.googleapis.com/css2?family=Dancing+Script:wght@400&display=swap" rel="stylesheet">
<style>
  :root {
    --board: #2e221c;
    --paper: #ffffff;
    --title: #5a9ec6;
    --ink: #7d8b95;
    --violet: #8a3f93;
    --teal: #2f8f86;
    --pink: #e0508e;
    --crimson: #c8213f;
    --lavender: #c9b3de;
    --sky: #2f8fd6;
    --navy: #27305a;
    --gold: #b48a46;
    --orange: #f08a1e;
    --sea: #7ccfc9;
    --lime: #8cc63f;
    --purple: #6a4fa3;
  }
  * { box-sizing: border-box; margin: 0; padding: 0; }
  html, body { width: 1200px; height: 790px; overflow: hidden; }
  body { background: var(--board); }

  .card-board {
    width: 1200px; height: 790px;
    padding: 38px 29px;
    display: grid;
    grid-template-columns: repeat(5, 213px);
    grid-template-rows: repeat(4, 164px);
    gap: 19px;
  }
  .card { position: relative; overflow: hidden; background: var(--paper); }
  .deco { position: absolute; }

  .verse {
    position: absolute; z-index: 1;
    left: 27%; top: 13%;
    font-family: "Dancing Script", cursive;
    font-weight: 400;
    color: var(--ink);
  }
  .verse h2 {
    font-family: "Dancing Script", cursive; font-weight: 400;
    font-size: 11px; line-height: 13px; color: var(--title);
    margin: 0 0 4px 10px;
  }
  .verse p { font-size: 6px; line-height: 8.4px; white-space: nowrap; }
  .verse p + p { margin-top: 5px; }

  /* Row 1 */
  .violet-swirl .band-l { left: 0; top: 0; width: 15%; height: 100%; background: linear-gradient(90deg, var(--violet), #c48bcc); border-radius: 0 60% 60% 0 / 0 50% 50% 0; }
  .violet-swirl .band-r { right: 0; top: 0; width: 10%; height: 100%; background: linear-gradient(270deg, var(--violet), #d6a7dc); }

  .teal-dots .band-l { left: 0; top: 0; width: 4%; height: 100%; background: var(--teal); }
  .teal-dots .band-r { right: 0; top: 0; width: 9%; height: 100%; background: var(--teal); }
  .teal-dots .flowers-tl { left: 4%; top: 0; width: 22%; height: 18%; background: linear-gradient(90deg, #f05a3c, #f7b733); }
  .teal-dots .flowers-br { right: 9%; bottom: 0; width: 30%; height: 22%; background: linear-gradient(90deg, #f7d58a, #9fd0ec); }

  .bubble-frame { background: linear-gradient(135deg, #f6a6c8, #b8e07a 35%, #7ec9ef 65%, #f57fb0); }
  .bubble-frame .inner { left: 8%; top: 9%; right: 8%; bottom: 9%; background: var(--paper); border-radius: 6px; }

  .crimson-floral { background: linear-gradient(160deg, var(--crimson), #ef5d7d); }
  .crimson-floral .inner { left: 5%; top: 14%; right: 5%; bottom: 10%; background: var(--paper); border-radius: 40% 40% 6px 6px / 18% 18% 6px 6px; }

  .lilac-garden .field-r { right: 0; top: 0; width: 30%; height: 100%; background: linear-gradient(180deg, #f3e9f7, var(--lavender)); }
  .lilac-garden .field-b { left: 0; bottom: 0; width: 70%; height: 24%; background: linear-gradient(90deg, #d4ebc6, #f3c8dc); }

  /* Row 2 */
  .rose-border .lace { left: 0; top: 0; width: 100%; height: 8%; background: #bfe3d8; }
  .rose-border .roses { left: 0; bottom: 0; width: 100%; height: 24%; background: linear-gradient(90deg, #8d7a88, #d9cad5, #8d7a88); }

  .sky-frame { background: linear-gradient(180deg, #69b8ef, var(--sky)); }
  .sky-frame .inner { left: 7%; top: 9%; right: 7%; bottom: 9%; background: var(--paper); }

  .night-glitter .strip-l { left: -8%; top: 0; width: 28%; height: 100%; background: linear-gradient(90deg, var(--navy), #5a5a8a, var(--gold)); transform: skewX(-14deg); }
  .night-glitter .strip-r { right: -6%; top: 0; width: 16%; height: 100%; background: linear-gradient(90deg, var(--gold), #6a5128); transform: skewX(-14deg); }

  .ember-swirl .top { left: 0; top: 0; width: 100%; height: 10%; background: linear-gradient(90deg, var(--crimson), var(--orange)); }
  .ember-swirl .bottom { left: 0; bottom: 0; width: 100%; height: 9%; background: linear-gradient(90deg, var(--orange), var(--crimson)); }
  .ember-swirl .flourish { right: 3%; top: 10%; width: 30%; height: 14%; background: linear-gradient(90deg, #fbe1d3, #f1b08e); }

  .pink-dots .band-l { left: 0; top: 0; width: 12%; height: 100%; background: linear-gradient(90deg, var(--pink), #f5b3d0); }
  .pink-dots .band-t { left: 0; top: 0; width: 100%; height: 9%; background: linear-gradient(90deg, var(--pink), #fbd9e8); }

  /* Row 3 */
  .sea-bloom { background: linear-gradient(135deg, var(--sea), var(--paper) 45%, var(--paper) 65%, var(--sea)); }
  .sea-bloom .flower { left: 0; bottom: 0; width: 22%; height: 34%; background: linear-gradient(180deg, #b7c6ee, #6f8ad2); }

  .wave-band .top { left: 0; top: 0; width: 100%; height: 12%; background: linear-gradient(180deg, #9bd0ef, var(--paper)); }
  .wave-band .bottom { left: 0; bottom: 0; width: 100%; height: 20%; background: linear-gradient(90deg, var(--lime), #2aa6c8, var(--sky)); border-radius: 60% 40% 0 0 / 40% 30% 0 0; }

  .ornate-navy { background: #efe6d6; }
  .ornate-navy .inner { left: 8%; top: 11%; right: 8%; bottom: 11%; background: var(--paper); border: 2px solid var(--navy); border-radius: 22px; }
  .ornate-navy .crest-t, .ornate-navy .crest-b { left: 32%; width: 36%; height: 9%; background: linear-gradient(90deg, #4a5590, var(--navy), #4a5590); }
  .ornate-navy .crest-t { top: 2%; }
  .ornate-navy .crest-b { bottom: 2%; }

  .rainbow-stripe .top { left: 0; top: 0; width: 100%; height: 9%; background: linear-gradient(90deg, #e84b3c, #f6a623, #f8e71c, #7ed321, #4ab3e6, #9b59b6, #e84b8a); }
  .rainbow-stripe .side { right: 0; bottom: 0; width: 26%; height: 40%; background: linear-gradient(90deg, #e84b3c, #f6a623, #7ed321, #4ab3e6, #9b59b6); }

  .sunset-curve .frame { left: 5%; top: 6%; right: 5%; bottom: 6%; border: 3px solid var(--orange); border-radius: 30px 8px 30px 8px; }
  .sunset-curve .frame-in { left: 8%; top: 10%; right: 8%; bottom: 10%; border: 2px solid #3fa7c9; border-radius: 26px 6px 26px 6px; }

  /* Row 4 */
  .denim-frame { background: linear-gradient(180deg, #2763b0, #173f80); }
  .denim-frame .inner { left: 6%; top: 8%; right: 6%; bottom: 14%; background: var(--paper); border-radius: 4px 4px 40% 40% / 4px 4px 12% 12%; }

  .gold-coins .corner-tr { right: 0; top: 0; width: 22%; height: 30%; background: linear-gradient(180deg, #d8bb84, var(--gold)); }
  .gold-coins .corner-bl { left: 0; bottom: 0; width: 48%; height: 22%; background: linear-gradient(90deg, #8f6a30, #d8bb84); }

  .mosaic-frame { background: linear-gradient(135deg, var(--orange), var(--crimson) 50%, #f7c23c); }
  .mosaic-frame .inner { left: 10%; top: 12%; right: 10%; bottom: 18%; background: linear-gradient(180deg, var(--paper), #fbe8d5); }

  .ribbon-lines .corner { left: 0; top: 0; width: 30%; height: 20%; background: linear-gradient(135deg, #8f7cc4, #c9bfe4); }
  .ribbon-lines .base { left: 0; bottom: 0; width: 100%; height: 7%; background: var(--purple); }

  .color-rings .rings-l { left: 0; top: 0; width: 17%; height: 100%; background: linear-gradient(180deg, #b584cc, #f29cc0, #f8c77a, #b5e08c); }
  .color-rings .rings-r { right: 0; top: 0; width: 17%; height: 100%; background: linear-gradient(180deg, #b5e08c, #9ad2ef, #f29cc0, #f8c77a); }
</style>
</head>
<body>
<main class="card-board">

  <article class="card violet-swirl">
    <div class="deco band-l" role="img" aria-label="Purple swirl ornament"></div>
    <div class="deco band-r" role="img" aria-label="Purple swirl ornament"></div>
    <div class="verse"><h2>A Special World</h2><p>A special word for you and me<br>A special bond we should see<br>It wakes us up to the sunrise<br>And holds us through the night.</p><p>Its fingers spread like flowers gold<br>Gently reaching out to the field<br>Like shining threads it binds us fast<br>Proving love has no need to last</p></div>
  </article>

  <article class="card teal-dots">
    <div class="deco band-l"></div>
    <div class="deco band-r" role="img" aria-label="Teal polka dot border"></div>
    <div class="deco flowers-tl" role="img" aria-label="Cluster of bright flowers"></div>
    <div class="deco flowers-br" role="img" aria-label="Flowers and swirls"></div>
    <div class="verse"><h2>A Special World</h2><p>A special word for you and me<br>A special bond we should see<br>It wakes us up to the sunrise<br>And holds us through the night.</p><p>Its fingers spread like flowers gold<br>Gently reaching out to the field<br>Like shining threads it binds us fast<br>Proving love has no need to last</p></div>
  </article>

  <article class="card bubble-frame" role="img" aria-label="Frame of colourful overlapping circles">
    <div class="deco inner"></div>
    <div class="verse"><h2>A Special World</h2><p>A special word for you and me<br>A special bond we should see<br>It wakes us up to the sunrise<br>And holds us through the night.</p><p>Its fingers spread like flowers gold<br>Gently reaching out to the field<br>Like shining threads it binds us fast<br>Proving love has no need to last</p></div>
  </article>

  <article class="card crimson-floral" role="img" aria-label="Red frame with white flower pattern">
    <div class="deco inner"></div>
    <div class="verse"><h2>A Special World</h2><p>A special word for you and me<br>A special bond we should see<br>It wakes us up to the sunrise<br>And holds us through the night.</p><p>Its fingers spread like flowers gold<br>Gently reaching out to the field<br>Like shining threads it binds us fast<br>Proving love has no need to last</p></div>
  </article>

  <article class="card lilac-garden">
    <div class="deco field-r" role="img" aria-label="Pastel flower garden"></div>
    <div class="deco field-b" role="img" aria-label="Pastel flower stems"></div>
    <div class="verse"><h2>A Special World</h2><p>A special word for you and me<br>A special bond we should see<br>It wakes us up to the sunrise<br>And holds us through the night.</p><p>Its fingers spread like flowers gold<br>Gently reaching out to the field<br>Like shining threads it binds us fast<br>Proving love has no need to last</p></div>
  </article>

  <article class="card rose-border">
    <div class="deco lace" role="img" aria-label="Mint lace trim"></div>
    <div class="deco roses" role="img" aria-label="Row of roses"></div>
    <div class="verse"><h2>A Special World</h2><p>A special word for you and me<br>A special bond we should see<br>It wakes us up to the sunrise<br>And holds us through the night.</p><p>Its fingers spread like flowers gold<br>Gently reaching out to the field<br>Like shining threads it binds us fast<br>Proving love has no need to last</p></div>
  </article>

  <article class="card sky-frame" role="img" aria-label="Blue dotted frame">
    <div class="deco inner"></div>
    <div class="verse"><h2>A Special World</h2><p>A special word for you and me<br>A special bond we should see<br>It wakes us up to the sunrise<br>And holds us through the night.</p><p>Its fingers spread like flowers gold<br>Gently reaching out to the field<br>Like shining threads it binds us fast<br>Proving love has no need to last</p></div>
  </article>

  <article class="card night-glitter">
    <div class="deco strip-l" role="img" aria-label="Navy and gold glitter strip"></div>
    <div class="deco strip-r" role="img" aria-label="Gold glitter strip"></div>
    <div class="verse"><h2>A Special World</h2><p>A special word for you and me<br>A special bond we should see<br>It wakes us up to the sunrise<br>And holds us through the night.</p><p>Its fingers spread like flowers gold<br>Gently reaching out to the field<br>Like shining threads it binds us fast<br>Proving love has no need to last</p></div>
  </article>

  <article class="card ember-swirl">
    <div class="deco top"></div>
    <div class="deco bottom"></div>
    <div class="deco flourish" role="img" aria-label="Red flourish swirl"></div>
    <div class="verse"><h2>A Special World</h2><p>A special word for you and me<br>A special bond we should see<br>It wakes us up to the sunrise<br>And holds us through the night.</p><p>Its fingers spread like flowers gold<br>Gently reaching out to the field<br>Like shining threads it binds us fast<br>Proving love has no need to last</p></div>
  </article>

  <article class="card pink-dots">
    <div class="deco band-l" role="img" aria-label="Pink dotted border with branch"></div>
    <div class="deco band-t"></div>
    <div class="verse"><h2>A Special World</h2><p>A special word for you and me<br>A special bond we should see<br>It wakes us up to the sunrise<br>And holds us through the night.</p><p>Its fingers spread like flowers gold<br>Gently reaching out to the field<br>Like shining threads it binds us fast<br>Proving love has no need to last</p></div>
  </article>

  <article class="card sea-bloom">
    <div class="deco flower" role="img" aria-label="Blue lily flowers"></div>
    <div class="verse"><h2>A Special World</h2><p>A special word for you and me<br>A special bond we should see<br>It wakes us up to the sunrise<br>And holds us through the night.</p><p>Its fingers spread like flowers gold<br>Gently reaching out to the field<br>Like shining threads it binds us fast<br>Proving love has no need to last</p></div>
  </article>

  <article class="card wave-band">
    <div class="deco top"></div>
    <div class="deco bottom" role="img" aria-label="Green and blue flowing waves"></div>
    <div class="verse"><h2>A Special World</h2><p>A special word for you and me<br>A special bond we should see<br>It wakes us up to the sunrise<br>And holds us through the night.</p><p>Its fingers spread like flowers gold<br>Gently reaching out to the field<br>Like shining threads it binds us fast<br>Proving love has no need to last</p></div>
  </article>

  <article class="card ornate-navy">
    <div class="deco inner"></div>
    <div class="deco crest-t" role="img" aria-label="Navy floral ornament"></div>
    <div class="deco crest-b" role="img" aria-label="Navy floral ornament"></div>
    <div class="verse"><h2>A Special World</h2><p>A special word for you and me<br>A special bond we should see<br>It wakes us up to the sunrise<br>And holds us through the night.</p><p>Its fingers spread like flowers gold<br>Gently reaching out to the field<br>Like shining threads it binds us fast<br>Proving love has no need to last</p></div>
  </article>

  <article class="card rainbow-stripe">
    <div class="deco top" role="img" aria-label="Rainbow stripe band"></div>
    <div class="deco side" role="img" aria-label="Rainbow stripe pattern"></div>
    <div class="verse"><h2>A Special World</h2><p>A special word for you and me<br>A special bond we should see<br>It wakes us up to the sunrise<br>And holds us through the night.</p><p>Its fingers spread like flowers gold<br>Gently reaching out to the field<br>Like shining threads it binds us fast<br>Proving love has no need to last</p></div>
  </article>

  <article class="card sunset-curve">
    <div class="deco frame"></div>
    <div class="deco frame-in"></div>
    <div class="verse"><h2>A Special World</h2><p>A special word for you and me<br>A special bond we should see<br>It wakes us up to the sunrise<br>And holds us through the night.</p><p>Its fingers spread like flowers gold<br>Gently reaching out to the field<br>Like shining threads it binds us fast<br>Proving love has no need to last</p></div>
  </article>

  <article class="card denim-frame" role="img" aria-label="Blue denim frame">
    <div class="deco inner"></div>
    <div class="verse"><h2>A Special World</h2><p>A special word for you and me<br>A special bond we should see<br>It wakes us up to the sunrise<br>And holds us through the night.</p><p>Its fingers spread like flowers gold<br>Gently reaching out to the field<br>Like shining threads it binds us fast<br>Proving love has no need to last</p></div>
  </article>

  <article class="card gold-coins">
    <div class="deco corner-tr" role="img" aria-label="Gold circle ornaments"></div>
    <div class="deco corner-bl" role="img" aria-label="Gold circle ornaments"></div>
    <div class="verse"><h2>A Special World</h2><p>A special word for you and me<br>A special bond we should see<br>It wakes us up to the sunrise<br>And holds us through the night.</p><p>Its fingers spread like flowers gold<br>Gently reaching out to the field<br>Like shining threads it binds us fast<br>Proving love has no need to last</p></div>
  </article>

  <article class="card mosaic-frame" role="img" aria-label="Orange and red diamond mosaic frame">
    <div class="deco inner"></div>
    <div class="verse"><h2>A Special World</h2><p>A special word for you and me<br>A special bond we should see<br>It wakes us up to the sunrise<br>And holds us through the night.</p><p>Its fingers spread like flowers gold<br>Gently reaching out to the field<br>Like shining threads it binds us fast<br>Proving love has no need to last</p></div>
  </article>

  <article class="card ribbon-lines">
    <div class="deco corner" role="img" aria-label="Purple line pattern with red ribbon bow"></div>
    <div class="deco base" role="img" aria-label="Purple patterned strip"></div>
    <div class="verse"><h2>A Special World</h2><p>A special word for you and me<br>A special bond we should see<br>It wakes us up to the sunrise<br>And holds us through the night.</p><p>Its fingers spread like flowers gold<br>Gently reaching out to the field<br>Like shining threads it binds us fast<br>Proving love has no need to last</p></div>
  </article>

  <article class="card color-rings">
    <div class="deco rings-l" role="img" aria-label="Colourful concentric rings"></div>
    <div class="deco rings-r" role="img" aria-label="Colourful concentric rings"></div>
    <div class="verse"><h2>A Special World</h2><p>A special word for you and me<br>A special bond we should see<br>It wakes us up to the sunrise<br>And holds us through the night.</p><p>Its fingers spread like flowers gold<br>Gently reaching out to the field<br>Like shining threads it binds us fast<br>Proving love has no need to last</p></div>
  </article>

</main>
</body>
</html>
```